An eCommerce Business Needs a Wordpress Web Design and Development

We need a website design and development for a new eCommerce business based in New York called "Velvet Orra". We sell items that are based on satisfying multi-sensory pathways of the person, as we believe that all is interconnected forming the Universal Language. All our products are made of raw natural elements from earth or the cosmos. The final design should communicate visual-perceptive pathways that produce harmonious effects and creativity.
Updates

Dear Designers, Please accept my sincere apology for my delayed response. I am currently in the midst of extensive business travelling while at the same time gathering feedback from online polling with friends as the website potential end-users. I shall get back to you by May 12 or sooner. Thank you for your understanding.

Target Market(s)

Art, fossils, minerals and numismatic collectors.

Industry/Entity Type

Online Shopping

Coding

Coded - Design and coding required

Number of Pages Required

5+ page

Font styles to use
Sans Serif
Script

Colors

Designer to choose colors to be used in the design.

Requirements
Must have
• - Simple and clean design.
• - Desktop and mobile device friendly.
• - Photos and images of string musical instruments, crystals, numismatics and cultural artefacts.
• - A blog page.
• - A check-out cart for online shopping and payment. Example: https://store.plumwick.com
• - Standard links to social media.

```html
<!DOCTYPE html>
<html lang="en">
<head>
<meta charset="utf-8">
<title>Velvet Orra — Musical Instruments, Crystals &amp; Collectibles</title>
<link rel="stylesheet" href="https://fonts.googleapis.com/css2?family=Lato:wght@400;700;900&family=Kaushan+Script&family=Libre+Baskerville:wght@400;700&display=swap">
<style>
:root{
  --white:#ffffff;
  --navy:#0b4f96;
  --link-blue:#1b4f8a;
  --gold:#c9a227;
  --gold-bright:#f0c63a;
  --gold-soft:#a88a2c;
  --ink:#050608;
  --title-blue:#1d5fb0;
  --accent-blue:#7fb0ff;
  --card-border:#d4a626;
  --text-light:#f3f5f8;
  --sans:'Lato', Arial, sans-serif;
  --serif:'Libre Baskerville', Georgia, serif;
  --script:'Kaushan Script', cursive;
}
*{box-sizing:border-box;margin:0;padding:0}
html,body{width:868px;height:1200px;overflow:hidden;background:var(--ink)}
.page{position:relative;width:868px;height:1200px;overflow:hidden;font-family:var(--sans)}

/* header */
.site-header{position:absolute;left:0;top:0;width:868px;height:94px;background:var(--white)}
.brand{position:absolute;left:118px;top:33px;display:flex;align-items:center;gap:6px;font-family:var(--sans);font-weight:700;font-size:17px;color:var(--link-blue);letter-spacing:.5px}
.brand-dot{width:9px;height:9px;border-radius:50%;background:var(--navy)}
.search{position:absolute;left:296px;top:34px;width:158px;height:20px;border:2px solid var(--navy);border-radius:4px;background:var(--white)}
.search-text{position:absolute;left:10px;top:2px;font-size:9px;color:#b8bcc4}
.search-btn{position:absolute;right:-2px;top:-2px;width:20px;height:20px;background:var(--navy);border-radius:0 4px 4px 0}
.top-nav{position:absolute;top:22px;left:513px;display:flex;gap:13px;font-size:7.5px;color:var(--link-blue);letter-spacing:.2px}
.top-nav .active{color:var(--gold-soft)}
.social{position:absolute;display:flex}
.social span{display:block;border-radius:50%}
.social-top{left:602px;top:63px;gap:9px}
.social-top span{width:16px;height:16px;background:var(--gold-soft)}
.cart{position:absolute;left:703px;top:62px}
.cart-total{position:absolute;left:732px;top:62px;font-size:7px;color:#8a5a12;text-align:center;line-height:11px}

/* category nav */
.cat-nav{position:absolute;left:0;top:94px;width:868px;height:33px;background:var(--navy)}
.cat-nav a{position:absolute;top:11px;font-size:8.5px;font-weight:900;color:var(--white);letter-spacing:.4px;text-decoration:none}
.cat-nav .current{color:var(--gold)}
.dropdown{position:absolute;left:206px;top:127px;width:96px;height:57px;background:var(--white);z-index:5;padding:11px 0 0 14px}
.dropdown li{list-style:none;font-size:7px;color:var(--gold-soft);line-height:13px;font-weight:700}

/* hero */
.hero{position:absolute;left:0;top:127px;width:868px;height:330px;background:radial-gradient(ellipse 260px 240px at 434px 170px,#2a2a2c 0%,#0c0c0e 60%,#050507 100%)}
.card{position:absolute;border:1.5px solid var(--card-border);background:linear-gradient(135deg,#141414 0 16%,#5e5e5e 16% 52%,#7a7a7a 52% 56%,#4c4c4c 56% 84%,#131313 84%)}
.card-media{position:absolute;border-radius:30px 30px 40px 40px}
.card-title{position:absolute;font-family:var(--serif);color:var(--white);white-space:nowrap;text-shadow:0 1px 2px rgba(0,0,0,.6)}
.card-title em{font-style:normal;color:var(--accent-blue)}
.card-title i{font-style:normal;color:var(--gold-bright)}
.btn-shop{position:absolute;background:var(--white);border:1.5px solid var(--card-border);font-family:var(--serif);font-weight:700;color:#222;display:flex;align-items:center;justify-content:center;letter-spacing:.6px}
.sale{position:absolute;left:530px;top:150px;width:66px;height:66px}
.dots{position:absolute;top:396px;left:414px;display:flex;gap:4px}
.dots span{width:8px;height:8px;border:1.5px solid var(--gold);border-radius:50%}

/* about */
.about{position:absolute;left:0;top:400px;width:868px;height:616px;background:linear-gradient(180deg,#3a5375 0%,#2c4565 35%,#263f5e 60%,#2b4566 100%)}
.crystals{position:absolute;left:0;top:800px;width:868px;height:216px;background:
  radial-gradient(ellipse 200px 90px at 150px 130px,rgba(140,170,220,.55),rgba(140,170,220,0) 70%),
  radial-gradient(ellipse 220px 100px at 690px 110px,rgba(150,180,230,.55),rgba(150,180,230,0) 70%),
  radial-gradient(ellipse 180px 80px at 420px 160px,rgba(110,140,200,.5),rgba(110,140,200,0) 70%),
  linear-gradient(180deg,rgba(43,69,102,0) 0%,#4d6c9e 35%,#5e7fb6 60%,#3f5c8c 100%)}
.curve{position:absolute;left:0;top:400px}
.about-title{position:absolute;top:458px;left:0;width:868px;text-align:center;font-family:var(--script);font-size:25px;font-weight:400;color:var(--title-blue)}
.rule{position:absolute;top:478px;height:1px;background:var(--gold-soft);width:99px}
.about-copy{position:absolute;left:112px;width:644px;text-align:center;color:var(--text-light);font-size:13.4px;line-height:26px;letter-spacing:.35px}
.about-copy .brand-word{color:var(--gold)}

/* footer */
.site-footer{position:absolute;left:0;top:1016px;width:868px;height:184px;background:radial-gradient(ellipse 220px 150px at 440px 90px,#3a1a24 0%,#120a10 50%,#050507 100%);border-top:1px solid #2b3a55}
.foot-nav{position:absolute;top:43px;left:0;width:868px;display:flex;justify-content:center;gap:13px;font-family:var(--serif);font-size:7.5px;color:var(--white)}
.foot-nav .active{color:var(--gold)}
.social-foot{left:399px;top:78px;gap:8px}
.social-foot span{width:17px;height:17px;background:#d8d8d8}
</style>
</head>
<body>
<div class="page">

  <header class="site-header">
    <div class="brand"><span class="brand-dot"></span>Velvet Orra</div>
    <div class="search">
      <span class="search-text">search</span>
      <span class="search-btn">
        <svg width="20" height="20" viewBox="0 0 20 20"><circle cx="9" cy="9" r="4" fill="none" stroke="#fff" stroke-width="1.6"/><line x1="12" y1="12" x2="15" y2="15" stroke="#fff" stroke-width="1.8"/></svg>
      </span>
    </div>
    <nav class="top-nav">
      <span>HOME</span><span>STORE</span><span>NEED HELP?</span><span class="active">BLOG</span><span>CONTACT</span><span>LOG IN</span>
    </nav>
    <div class="social social-top"><span></span><span></span><span></span></div>
    <svg class="cart" width="22" height="20" viewBox="0 0 22 20">
      <path d="M1 7 H21 L18 19 H4 Z" fill="#c9a227"/>
      <path d="M6 7 L10 1 M16 7 L12 1" stroke="#c9a227" stroke-width="1.6" fill="none"/>
    </svg>
    <div class="cart-total">200 $<br>3</div>
  </header>

  <nav class="cat-nav">
    <a class="current" style="left:162px">MUSICAL INSTRUMENTS ⌄</a>
    <a style="left:302px">CRYSTALS ⌄</a>
    <a style="left:378px">NUMISMATIC COLLECTIBLES</a>
    <a style="left:534px">CULTURAL ARTIFACTS</a>
    <a style="left:662px">ABOUT US</a>
  </nav>
  <ul class="dropdown"><li>GUITAR</li><li>VIOLIN</li><li>PIANO</li></ul>

  <section class="hero" role="img" aria-label="Dark stage photograph of an electric guitar body and strings"></section>

  <div class="card" style="left:118px;top:230px;width:152px;height:114px">
    <div class="card-media" role="img" aria-label="Acoustic wood guitar" style="left:22px;top:8px;width:32px;height:98px;background:linear-gradient(180deg,#3a2a18 0 45%,#c06a18 60%,#5a2e0a 100%)"></div>
    <div class="card-title" style="left:84px;top:35px;font-size:7px">Wood <em>Guitar</em></div>
    <div class="card-title" style="left:66px;top:47px;font-size:6.5px">10% off Only <i>This Week</i></div>
    <div class="btn-shop" style="left:71px;top:64px;width:68px;height:20px;font-size:6.5px">SHOP NOW</div>
  </div>

  <div class="card" style="left:290px;top:165px;width:286px;height:213px">
    <div class="card-media" role="img" aria-label="Black electric guitar" style="left:34px;top:16px;width:80px;height:190px;background:linear-gradient(180deg,#2a2a2a 0 45%,#050505 55%,#1a1a1a 100%)"></div>
    <div class="card-title" style="left:157px;top:74px;font-size:12px">Luxurious <em>Guitar</em></div>
    <div class="card-title" style="left:172px;top:94px;font-size:14px">20% <i>Off</i></div>
    <div class="btn-shop" style="left:139px;top:125px;width:129px;height:25px;font-size:8.5px">SHOP NOW</div>
  </div>

  <div class="card" style="left:598px;top:230px;width:152px;height:114px">
    <div class="card-media" role="img" aria-label="Blue electric guitar" style="left:14px;top:10px;width:40px;height:96px;background:linear-gradient(180deg,#3a4a66 0 45%,#1a58b0 60%,#0d3a7a 100%)"></div>
    <div class="card-title" style="left:84px;top:35px;font-size:7px">Magic <em>Guitar</em></div>
    <div class="card-title" style="left:66px;top:47px;font-size:6.5px">50% off Only <i>This Week</i></div>
    <div class="btn-shop" style="left:70px;top:64px;width:68px;height:20px;font-size:6.5px">SHOP NOW</div>
  </div>

  <svg class="sale" viewBox="0 0 66 66">
    <polygon points="33,2 40,18 58,12 50,28 64,40 46,44 44,62 33,50 22,62 20,44 2,40 16,28 8,12 26,18" fill="#f2cc28"/>
    <text x="33" y="37" text-anchor="middle" font-family="Lato, sans-serif" font-weight="700" font-size="10" fill="#7a5a08">Sale</text>
  </svg>
  <div class="dots"><span></span><span></span><span></span></div>

  <section class="about" role="img" aria-label="Blue photograph of a guitarist silhouette"></section>
  <div class="crystals" role="img" aria-label="Bed of pale blue crystals"></div>
  <svg class="curve" width="868" height="60" viewBox="0 0 868 60"><path d="M0 0 H868 V48 Q434 -16 0 48 Z" fill="#060607"/></svg>

  <h2 class="about-title">About Us</h2>
  <span class="rule" style="left:277px"></span>
  <span class="rule" style="left:496px"></span>

  <p class="about-copy" style="top:522px"><span class="brand-word">Velvet Orra</span> is a dedicated company, which foundation is based on an integrative view of the Universe. We seek items from all over the world, carefully selected to meet high standards of our merchandise. We sell items that are based on satisfying multi-sensory pathways of the person, as we believe that all is interconnected forming the Universal Language. All our products are made of raw natural elements from earth or the cosmos.</p>
  <p class="about-copy" style="top:685px">Although some of the effects of these raw elements are yet to be fully understood or detected by our current methods of scientific measurements; nonetheless, these natural elements are beautiful, mysterious, pleasant and conducive to amplify, direct and balance the life-force in a person’s body and surroundings. We hope through our products you will discover that working with organic and natural elements is a natural way to improve one’s wellbeing.</p>

  <footer class="site-footer" role="img" aria-label="Dark concert photograph with faint crystal shapes">
    <nav class="foot-nav">
      <span>HOME</span><span>STORE</span><span>NEED HELP?</span><span class="active">BLOG</span><span>CONTACT</span><span>LOG IN</span>
    </nav>
    <div class="social social-foot"><span></span><span></span><span></span></div>
  </footer>

</div>
</body>
</html>
```